Real Estate Website

We have a an existing website - harborkeyhomes.com.au which we want redesigned.

We want it to look more like the design/style of https://www.stallworth.com.au/

```html
<!DOCTYPE html>
<html lang="en">
<head>
<meta charset="utf-8">
<title>Harborkey Homes</title>
<link rel="stylesheet" href="https://fonts.googleapis.com/css2?family=Lato:ital,wght@0,400;0,700;1,400&family=Questrial&display=swap">
<style>
:root{
  --navy:#0b1a33;
  --navy-deep:#08162b;
  --teal:#0e6a7a;
  --teal-light:#1a8a99;
  --ink:#1a1a1a;
  --muted:#5b6270;
  --pale:#eef3fa;
  --star:#f0b323;
  --white:#ffffff;
}
*{box-sizing:border-box;margin:0;padding:0}
html,body{width:1200px;height:3343px;overflow:hidden}
body{position:relative;font-family:'Lato',sans-serif;color:var(--ink);background:var(--white)}
.display{font-family:'Questrial',sans-serif}
.abs{position:absolute}

/* header */
.site-header{position:absolute;left:0;top:0;width:1200px;height:66px;background:var(--navy);display:flex;align-items:center}
.brand{position:absolute;left:143px;display:flex;align-items:center;gap:10px;color:var(--white);font-size:24px;letter-spacing:1px}
.brand-dot{width:12px;height:12px;border-radius:50%;background:var(--teal-light)}
.main-nav{position:absolute;left:432px;display:flex;gap:21px;font-size:11px;color:var(--white)}
.main-nav a{color:inherit;text-decoration:none;padding-bottom:7px}
.main-nav a.active{border-bottom:2px solid var(--teal-light)}
.header-phone{position:absolute;left:928px;display:flex;align-items:center;gap:6px;color:var(--white);font-weight:700;font-size:16px}

/* hero */
.hero{position:absolute;left:0;top:66px;width:1200px;height:581px;background:linear-gradient(100deg,#3a3d44 0%,#6f7787 35%,#5f86b8 65%,#3f6fa8 100%)}
.hero-title{position:absolute;left:143px;top:150px;color:var(--white);font-size:68px;line-height:68px;font-weight:700}
.search{position:absolute;display:flex;align-items:center;background:var(--white);border-radius:26px;height:52px;width:506px;padding:3px;box-shadow:0 2px 8px rgba(0,0,0,.15)}
.search span{flex:1;padding-left:33px;font-size:13px;color:#444}
.search .btn{height:46px;width:155px;border-radius:23px;background:var(--teal);color:var(--white);font-size:11px;font-weight:700;display:flex;align-items:center;justify-content:center}
.hero-dots{position:absolute;left:1127px;top:232px;display:flex;flex-direction:column;gap:11px}
.hero-dots i{width:8px;height:8px;border-radius:50%;background:var(--white)}
.hero-dots i.on{background:var(--teal-light)}

.quick-links{position:absolute;left:143px;top:553px;width:913px;height:190px;display:flex;gap:2px;background:#e5e5e5;box-shadow:0 4px 10px rgba(0,0,0,.12)}
.quick-link{flex:1;background:var(--white);display:flex;flex-direction:column;align-items:center;padding-top:24px}
.quick-link svg{width:92px;height:92px}
.quick-link p{margin-top:26px;font-size:14px;font-weight:700}

.section-title{position:absolute;left:0;width:1200px;text-align:center;font-size:42px;font-weight:700}

/* featured */
.feature{position:absolute;top:948px;width:446px;height:330px;border-radius:3px;overflow:hidden}
.feature .photo{position:absolute;inset:0;background:linear-gradient(180deg,#cfcac2 0%,#a9a39b 50%,#2b2a28 85%,#111 100%)}
.tag{position:absolute;background:var(--teal);color:var(--white);font-weight:700;font-size:14px;padding:5px 8px}
.feature h3{position:absolute;left:38px;bottom:58px;color:var(--white);font-size:23px;line-height:22px;font-weight:700}
.feature .addr{position:absolute;left:38px;bottom:28px;color:var(--white);font-size:10px;display:flex;gap:6px;align-items:center}

/* recent sales */
.recent{position:absolute;left:0;top:1372px;width:1200px;height:666px;background:var(--pale)}
.sale{position:absolute;top:183px;width:297px;height:300px;background:var(--white);border:1px solid #d7dce3;border-radius:3px;padding:6px}
.sale .photo{height:160px;background:linear-gradient(135deg,#e8e4dc,#b8b0a2)}
.sale .tag{top:12px;right:12px;font-size:15px;padding:3px 8px}
.sale h4{margin:32px 20px 0;font-size:18px;line-height:23px;font-weight:400}
.specs{position:absolute;left:26px;top:257px;display:flex;gap:14px;font-size:14px;color:var(--teal)}
.specs span{display:flex;align-items:center;gap:6px}
.circle-arrow{position:absolute;width:44px;height:44px;border-radius:50%;border:1.5px solid #444;background:var(--white);display:flex;align-items:center;justify-content:center}
.pill{position:absolute;background:var(--teal);color:var(--white);border-radius:26px;font-size:11px;font-weight:700;display:flex;align-items:center;justify-content:center}

/* testimonials */
.testimonial{position:absolute;top:2243px;width:330px}
.avatar{width:144px;height:144px;border-radius:50%;background:linear-gradient(160deg,#9aa0a8,#3c4556)}
.stars{display:flex;gap:8px;margin:28px 0 0 0}
.quote{margin-top:14px;font-style:italic;font-size:11.5px;line-height:21.5px;color:var(--muted)}
.signoff{margin-top:16px;font-size:17px;color:var(--muted);font-style:italic}
.signoff b{font-style:normal;font-weight:400;color:var(--teal)}

/* cta */
.cta{position:absolute;left:0;top:2672px;width:1200px;height:290px;background:linear-gradient(90deg,#135a6b,#1b7282 50%,#125566)}
.cta h2{position:absolute;top:44px;width:1200px;text-align:center;color:var(--white);font-size:42px;line-height:51px;font-weight:700}
.cta .search .btn{background:var(--navy)}

/* footer */
.site-footer{position:absolute;left:0;top:2962px;width:1200px;height:381px;background:var(--navy-deep);color:var(--white)}
.footer-brand{position:absolute;left:143px;top:74px;font-size:40px;display:flex;align-items:center;gap:14px}
.footer-contact{position:absolute;left:143px;top:146px;font-size:13px;display:flex;flex-direction:column;gap:15px}
.footer-contact div{display:flex;gap:14px;align-items:center}
.footer-col h5{font-size:18px;font-weight:700;margin-bottom:19px}
.footer-col ul{list-style:none;font-size:13px;display:flex;flex-direction:column;gap:16px}
.legal{position:absolute;left:143px;top:335px;font-size:12.5px}
.social{position:absolute;top:318px;width:34px;height:34px;border-radius:50%;background:var(--white)}
</style>
</head>
<body>

<header class="site-header">
  <div class="brand"><span class="brand-dot"></span><span>Harborkey Homes</span></div>
  <nav class="main-nav">
    <a class="active">HOME</a><a>BUYING</a><a>SELLING</a><a>RENTING</a><a>BLOG</a><a>ABOUT US</a><a>CONTACT US</a>
  </nav>
  <div class="header-phone">
    <svg width="15" height="15" viewBox="0 0 24 24"><path fill="#1a8a99" d="M6.6 10.8a15 15 0 0 0 6.6 6.6l2.2-2.2a1 1 0 0 1 1-.25 11.4 11.4 0 0 0 3.6.57 1 1 0 0 1 1 1V20a1 1 0 0 1-1 1A17 17 0 0 1 3 4a1 1 0 0 1 1-1h3.5a1 1 0 0 1 1 1c0 1.25.2 2.45.57 3.57a1 1 0 0 1-.25 1z"/></svg>
    02 9000 4417
  </div>
</header>

<section class="hero" role="img" aria-label="Apartment balcony overlooking a residential tower and city skyline">
  <h1 class="hero-title display">Harborkey<br>Homes</h1>
  <div class="search" style="left:145px;top:331px"><span>Search by Subrub</span><div class="btn">CHECK LOCATION</div></div>
  <div class="hero-dots"><i></i><i></i><i class="on"></i><i></i><i></i></div>
</section>

<nav class="quick-links">
  <div class="quick-link">
    <svg viewBox="0 0 92 92" fill="none" stroke="#0e6a7a" stroke-width="3"><circle cx="46" cy="26" r="18"/><path d="M46 16v11M46 32v2"/><path d="M20 88V60l26-18 26 18v28z"/><path d="M38 88V70h16v18"/></svg>
    <p>PROPERTY ALERT</p>
  </div>
  <div class="quick-link">
    <svg viewBox="0 0 92 92" fill="none" stroke="#0e6a7a" stroke-width="3"><path d="M8 86h76"/><rect x="14" y="56" width="10" height="30"/><rect x="30" y="44" width="10" height="42"/><rect x="46" y="50" width="10" height="36"/><path d="M14 42l22-18 14 10 16-16"/><circle cx="68" cy="30" r="14"/><path d="M72 24h-6a3 3 0 0 0 0 6h4a3 3 0 0 1 0 6h-6M68 20v20"/></svg>
    <p>MARKET APPRAISAL</p>
  </div>
  <div class="quick-link">
    <svg viewBox="0 0 92 92" fill="none" stroke="#0e6a7a" stroke-width="3"><circle cx="46" cy="30" r="13"/><circle cx="20" cy="38" r="10"/><circle cx="72" cy="38" r="10"/><path d="M24 84V66a22 22 0 0 1 44 0v18z"/><path d="M4 80V66a14 14 0 0 1 18-13M88 80V66a14 14 0 0 0-18-13"/></svg>
    <p>OUR TEAM</p>
  </div>
  <div class="quick-link">
    <svg viewBox="0 0 92 92" fill="none" stroke="#0e6a7a" stroke-width="3"><rect x="34" y="10" width="52" height="38" rx="2"/><path d="M34 12l26 20 26-20"/><path d="M14 22l10 -4 8 16-6 5a40 40 0 0 0 22 24l6-6 16 8-4 10c-30 2-54-22-52-53z"/></svg>
    <p>CONTACT US</p>
  </div>
</nav>

<h2 class="section-title display" style="top:832px">Featured Listings</h2>

<article class="feature" style="left:143px">
  <div class="photo" role="img" aria-label="Bright open-plan apartment living and dining room"></div>
  <div class="tag" style="top:16px;right:16px">For Sale $749,000</div>
  <h3>Modern Apartment!!</h3>
  <div class="addr"><svg width="10" height="12" viewBox="0 0 10 12"><path fill="#1a8a99" d="M5 0a4 4 0 0 0-4 4c0 3 4 8 4 8s4-5 4-8a4 4 0 0 0-4-4z"/></svg>607/24 Linden Street For Sale in ELMWO</div>
</article>
<article class="feature" style="left:610px">
  <div class="photo" role="img" aria-label="Renovated studio apartment with lounge and window"></div>
  <div class="tag" style="top:16px;right:16px">CONTACT AGENT</div>
  <h3>Newly Renovated Studio in<br>Excellent Location</h3>
  <div class="addr"><svg width="10" height="12" viewBox="0 0 10 12"><path fill="#1a8a99" d="M5 0a4 4 0 0 0-4 4c0 3 4 8 4 8s4-5 4-8a4 4 0 0 0-4-4z"/></svg>11/14 Garden Park Road For Rent in ASHF</div>
</article>

<section class="recent">
  <h2 class="section-title display" style="top:76px">Recent Sales</h2>
  <div class="circle-arrow" style="left:77px;top:310px"><svg width="14" height="14" viewBox="0 0 14 14"><path d="M9 2L4 7l5 5" fill="none" stroke="#333" stroke-width="2"/></svg></div>
  <div class="circle-arrow" style="left:1080px;top:310px"><svg width="14" height="14" viewBox="0 0 14 14"><path d="M5 2l5 5-5 5" fill="none" stroke="#333" stroke-width="2"/></svg></div>

  <article class="sale" style="left:143px">
    <div class="photo" role="img" aria-label="Sold apartment dining and living area"></div>
    <div class="tag">$670,000</div>
    <h4>Sold by Clara Reyes 0400 000 123 - $670,000</h4>
    <div class="specs"><span>▬ 1</span><span>◫ 1</span><span>◉ 1</span></div>
  </article>
  <article class="sale" style="left:451px">
    <div class="photo" role="img" aria-label="Modern apartment lounge with television"></div>
    <div class="tag">$670,000</div>
    <h4>Modern Apartment close to all Amenities</h4>
    <div class="specs"><span>▬ 1</span><span>◫ 1</span><span>◉ 1</span></div>
  </article>
  <article class="sale" style="left:759px">
    <div class="photo" role="img" aria-label="Warmly furnished living room with timber furniture" style="background:linear-gradient(135deg,#d9a53a,#8a4a2a)"></div>
    <div class="tag">$670,000</div>
    <h4>Great apartment for Investment or First Home!</h4>
    <div class="specs"><span>▬ 1</span><span>◫ 1</span><span>◉ 1</span></div>
  </article>

  <div class="pill" style="left:495px;top:526px;width:210px;height:52px">VIEW MORE RECENT SALES</div>
</section>

<h2 class="section-title display" style="top:2122px">What our clients say</h2>
<div class="circle-arrow" style="left:96px;top:2394px"><svg width="14" height="14" viewBox="0 0 14 14"><path d="M9 2L4 7l5 5" fill="none" stroke="#333" stroke-width="2"/></svg></div>
<div class="circle-arrow" style="left:1060px;top:2394px"><svg width="14" height="14" viewBox="0 0 14 14"><path d="M5 2l5 5-5 5" fill="none" stroke="#333" stroke-width="2"/></svg></div>

<article class="testimonial" style="left:221px">
  <div class="avatar" role="img" aria-label="Portrait of client"></div>
  <div class="stars"><svg width="110" height="15" viewBox="0 0 110 15"><g fill="#f0b323"><path id="st" d="M7.5 0l2.2 4.8 5.3.5-4 3.5 1.2 5.2-4.7-2.8L2.8 14l1.2-5.2-4-3.5 5.3-.5z"/><use href="#st" x="23"/><use href="#st" x="46"/><use href="#st" x="69"/><use href="#st" x="92"/></g></svg></div>
  <p class="quote">"We would like to thank Leon Marsh for his professionalism and efficiency during the sale of our house. We met Leon Marsh and we knew right away he was the person to sell our house. Leon was honest and personable and made some great suggestions prior to listing the house to attract more buyers"</p>
  <p class="signoff"><b>- Dear Leon</b>,Client name</p>
</article>
<article class="testimonial" style="left:669px">
  <div class="avatar" role="img" aria-label="Portrait of client"></div>
  <div class="stars"><svg width="110" height="15" viewBox="0 0 110 15"><g fill="#f0b323"><use href="#st"/><use href="#st" x="23"/><use href="#st" x="46"/><use href="#st" x="69"/><use href="#st" x="92"/></g></svg></div>
  <p class="quote">"My wife and I would like to take this opportunity to thank you for all your assistance and professionalism during the purchase of our new home in Westmere Park. Your professional attitude and attention to detail made our experience of purchasing a new home so much easier and your"</p>
  <p class="signoff"><b>- Dear Owen</b>,Client name</p>
</article>

<section class="cta">
  <h2 class="display">Check to see if your property is<br>eligible for the Harborkey Service</h2>
  <div class="search" style="left:347px;top:186px"><span>Search by Subrub</span><div class="btn">CHECK LOCATION</div></div>
</section>

<footer class="site-footer">
  <div class="footer-brand"><span class="brand-dot" style="width:16px;height:16px"></span><span>Harborkey Homes</span></div>
  <div class="footer-contact">
    <div><svg width="10" height="12" viewBox="0 0 10 12"><path fill="#1a8a99" d="M5 0a4 4 0 0 0-4 4c0 3 4 8 4 8s4-5 4-8a4 4 0 0 0-4-4z"/></svg>Shop 4, 88 Harbour Rd, Tidewater NSW 2020</div>
    <div><svg width="11" height="11" viewBox="0 0 24 24"><path fill="#1a8a99" d="M6.6 10.8a15 15 0 0 0 6.6 6.6l2.2-2.2a1 1 0 0 1 1-.25 11.4 11.4 0 0 0 3.6.57 1 1 0 0 1 1 1V20a1 1 0 0 1-1 1A17 17 0 0 1 3 4a1 1 0 0 1 1-1h3.5a1 1 0 0 1 1 1c0 1.25.2 2.45.57 3.57a1 1 0 0 1-.25 1z"/></svg>P: 02 9000 4417</div>
    <div><svg width="12" height="10" viewBox="0 0 12 10"><rect width="12" height="10" fill="#1a8a99"/><path d="M0 1l6 4 6-4" stroke="#08162b" fill="none"/></svg>E: enquiries@harborkeyhomes.com.au</div>
  </div>
  <div class="footer-col abs" style="left:601px;top:60px"><h5>BUYING</h5>
    <ul><li>Properties for Sale</li><li>Commercial for Sale</li><li>Land for Sale</li><li>Open Homes</li></ul></div>
  <div class="footer-col abs" style="left:769px;top:97px">
    <ul><li>Auction Timetable</li><li>Buying Tips</li><li>Sales Team</li><li>Property Alert</li></ul></div>
  <div class="footer-col abs" style="left:953px;top:60px"><h5>SELLING</h5>
    <ul><li>Selling Tips</li><li>Market Appraisal</li><li>Recent Sales</li><li>Testimonials</li></ul></div>
  <p class="legal">© 2021 Harborkey Homes.All Rights Reserved &nbsp;|&nbsp; Privacy Policy &nbsp;|&nbsp; Terms and use</p>
  <span class="social" style="left:978px" aria-label="Social profile"></span>
  <span class="social" style="left:1021px" aria-label="Social profile"></span>
</footer>

</body>
</html>
```